4R Capital business cards for a tech VC

We're starting a new Venture Capital that is focusing on bringing the best start ups from Israel to NYC
We need a business cards template for this that gives the sense of an entrepreneurial look
I don't want any religious signs on this even thought it's Israel
I'm looking for a techi feeling but not too crazy
The card should probably be in the same light blue as the logo and the logo in white

Target Market(s)

Investors

Industry/Entity Type

Tech

Contact Information for Business Card

The card needs to look slick and entrepreneurship like
The VC is focused on NYC and Tel Aviv so could be great to show something on the back side that is like NYC skyline or something like that
You can see the logo attached

Colors
0455a3
3276b5
85acd3
cedeed
eaf1f7

Requirements
Must have
• A very cool looking business card that shows we're a cutting edge tech VC with a focus on bringing start ups from Tel Aviv and leveraging the NYC ecosystem
Nice to have
• NYC skyline can be cool , maybe something that is connected to Tel Aviv

```html
<!DOCTYPE html>
<html lang="en">
<head>
<meta charset="utf-8">
<title>4R Capital Business Card</title>
<link href="https://fonts.googleapis.com/css2?family=Open+Sans:ital,wght@0,400;0,700;1,700&display=swap" rel="stylesheet">
<style>
  :root {
    --stage: #2f74b5;
    --brand-deep: #0455a3;
    --brand-mid: #3276b5;
    --brand-light: #85acd3;
    --sky: #5fc0f0;
    --mist: #cedeed;
    --paper: #ffffff;
    --paper-grey: #e4e6e8;
    --ink: #5a5f66;
    --ink-dark: #4a4d52;
  }
  * { margin: 0; padding: 0; box-sizing: border-box; }
  html, body { width: 1200px; height: 900px; overflow: hidden; }
  body {
    background: var(--stage);
    font-family: "Open Sans", Arial, sans-serif;
    position: relative;
  }
  .card {
    position: absolute;
    left: 300px;
    width: 600px;
    height: 340px;
    overflow: hidden;
    box-shadow: 0 10px 24px rgba(0, 40, 90, 0.35);
  }
  .card-back { top: 60px; }
  .card-front { top: 470px; }
  .card-art { position: absolute; inset: 0; width: 100%; height: 100%; }

  .wordmark {
    position: absolute;
    font-weight: 700;
    letter-spacing: 2px;
    line-height: 1;
    text-transform: uppercase;
    white-space: nowrap;
  }
  .card-back .wordmark {
    right: 40px;
    top: 70px;
    font-size: 54px;
    color: var(--paper);
  }
  .card-front .wordmark {
    left: 0;
    right: 0;
    top: 52px;
    text-align: center;
    font-size: 48px;
    color: var(--brand-mid);
    padding-left: 40px;
  }
  .web-address {
    position: absolute;
    left: 42px;
    bottom: 38px;
    font-size: 14px;
    font-weight: 700;
    font-style: italic;
    color: var(--ink-dark);
    letter-spacing: 0.5px;
  }

  .contact-list {
    position: absolute;
    left: 318px;
    top: 172px;
    list-style: none;
  }
  .contact-list li {
    display: flex;
    align-items: center;
    gap: 12px;
    height: 24px;
    font-size: 15px;
    color: var(--ink);
    margin-bottom: 4px;
    white-space: nowrap;
  }
  .contact-icon { width: 17px; height: 17px; flex: none; }

  .holder {
    position: absolute;
    left: 32px;
    bottom: 28px;
    color: var(--paper);
    white-space: nowrap;
  }
  .holder-name {
    font-size: 23px;
    font-weight: 700;
    font-style: italic;
    letter-spacing: 0.5px;
  }
  .holder-role {
    font-size: 16px;
    font-variant: small-caps;
    letter-spacing: 0.3px;
  }
</style>
</head>
<body>

<section class="card card-back" aria-label="Card back">
  <svg class="card-art" viewBox="0 0 600 340" preserveAspectRatio="none" aria-hidden="true">
    <defs>
      <linearGradient id="backBlue" x1="1" y1="0" x2="0.4" y2="1">
        <stop offset="0" stop-color="#66c4f2"/>
        <stop offset="0.5" stop-color="#3a8fd2"/>
        <stop offset="1" stop-color="#2f7fc4"/>
      </linearGradient>
      <linearGradient id="backGrey" x1="0" y1="0" x2="1" y2="1">
        <stop offset="0" stop-color="#f1f1f1"/>
        <stop offset="1" stop-color="#dcdcdc"/>
      </linearGradient>
    </defs>
    <rect width="600" height="340" fill="url(#backBlue)"/>
    <path d="M0 0 H118 C150 150 250 265 330 340 H0 Z" fill="#3a89cf"/>
    <path d="M0 0 H92 C130 150 240 260 316 340 H0 Z" fill="#7cc8f0"/>
    <path d="M0 0 H70 C112 150 220 255 300 340 H0 Z" fill="url(#backGrey)"/>
  </svg>
  <div class="wordmark">4R Capital</div>
  <div class="web-address">WWW.4RCAPITAL.COM</div>
</section>

<section class="card card-front" aria-label="Card front">
  <svg class="card-art" viewBox="0 0 600 340" preserveAspectRatio="none" aria-hidden="true">
    <defs>
      <linearGradient id="frontBlue" x1="0" y1="0" x2="0.6" y2="1">
        <stop offset="0" stop-color="#5dbdee"/>
        <stop offset="0.6" stop-color="#3382c6"/>
        <stop offset="1" stop-color="#2d7bc0"/>
      </linearGradient>
      <linearGradient id="cornerBlue" x1="0" y1="0" x2="1" y2="0">
        <stop offset="0" stop-color="#3f93d4"/>
        <stop offset="1" stop-color="#6fc9f3"/>
      </linearGradient>
    </defs>
    <rect width="600" height="340" fill="var(--paper)"/>
    <path d="M395 0 H600 V160 C540 80 470 20 395 0 Z" fill="url(#cornerBlue)"/>
    <path d="M0 0 H130 C150 160 260 290 390 340 H0 Z" fill="#e2e3e5"/>
    <path d="M0 0 H40 C80 170 220 290 370 340 H0 Z" fill="url(#frontBlue)"/>
    <path d="M40 0 H56 C96 160 230 280 370 340 C220 290 80 170 40 0 Z" fill="#ffffff"/>
  </svg>

  <div class="wordmark">4R Capital</div>

  <ul class="contact-list">
    <li>
      <svg class="contact-icon" viewBox="0 0 20 20" aria-hidden="true">
        <circle cx="10" cy="10" r="9" fill="none" stroke="var(--brand-mid)" stroke-width="1.5"/>
        <path d="M10 4.5a3.5 3.5 0 0 1 3.5 3.5c0 2.5-3.5 6.5-3.5 6.5S6.5 10.5 6.5 8A3.5 3.5 0 0 1 10 4.5z" fill="var(--brand-mid)"/>
        <circle cx="10" cy="8" r="1.3" fill="#fff"/>
      </svg>
      <span>PO Box 000 Northvale Vic 0000</span>
    </li>
    <li>
      <svg class="contact-icon" viewBox="0 0 20 20" aria-hidden="true">
        <circle cx="10" cy="10" r="9" fill="none" stroke="var(--brand-mid)" stroke-width="1.5"/>
        <path d="M5 9c0-2 10-2 10 0v1h-2.5V8.6h-5V10H5z M6.5 10.5h7l1 3.5h-9z" fill="var(--brand-mid)"/>
      </svg>
      <span>0300 555 019</span>
    </li>
    <li>
      <svg class="contact-icon" viewBox="0 0 20 20" aria-hidden="true">
        <circle cx="10" cy="10" r="9" fill="none" stroke="var(--brand-mid)" stroke-width="1.5"/>
        <rect x="5" y="6.5" width="10" height="7" fill="var(--brand-mid)"/>
        <path d="M5 6.5l5 4 5-4" fill="none" stroke="#fff" stroke-width="1"/>
      </svg>
      <span>INFO@4RCAPITAL.COM</span>
    </li>
    <li>
      <svg class="contact-icon" viewBox="0 0 20 20" aria-hidden="true">
        <circle cx="10" cy="10" r="9" fill="none" stroke="var(--brand-mid)" stroke-width="1.5"/>
        <circle cx="10" cy="10" r="5.5" fill="none" stroke="var(--brand-mid)" stroke-width="1"/>
        <ellipse cx="10" cy="10" rx="2.4" ry="5.5" fill="none" stroke="var(--brand-mid)" stroke-width="1"/>
        <path d="M4.5 10h11M5.3 7.3h9.4M5.3 12.7h9.4" stroke="var(--brand-mid)" stroke-width="0.9"/>
      </svg>
      <span>WWW.4RCAPITAL.COM</span>
    </li>
  </ul>

  <div class="holder">
    <div class="holder-name">DAN LEVAN</div>
    <div class="holder-role">Co-Founder &amp; Partner</div>
  </div>
</section>

</body>
</html>
```